Lantern Hour book needs a cover design

I need a front and back cover design that demonstrates a strong sense of possibility that trust can be repaired even if things look bleak. Repairing trust is difficult, but this book is full of wisdom, proven strategies, and doctoral research to help people strengthen relationships and improve trust. It can help any group: business, nonprofit, education, service. Showing diversity of groups and people is very important. For the cover title, there should be a play on words: "Lantern Hour: Is it? Possible" should have the words "is it?" crossed out and the words "It IS! should be replaced there in a striking way. Perhaps in red ink. For publishing purposes, book will be titled Lantern Hour: It IS Possible! Please see the attachment for an example. The book layout is approximately 260 pages.

Target Market(s)

A business self-help book, but the target is any person in a group that feels they have lost trust in each other. It can be just a normal person struggling in a volunteer group they are a part of, or a supervisor whose group is not working well together. It can be a leader who just wants their group to be stronger.

Industry/Entity Type

Business Management

Font styles to use
Other font styles liked:
• Allise - I believe is being used on the interior of the book for the title page and headings

Requirements
Must have
• Show hope and possibility in the midst of difficulty. Must have a play on the words in the title "Lantern Hour: Is it? Possible" with crossing out "is it?" with "It IS!" (see attached example) Must include the author's name: Marla Quinby, PhD Must include a smaller tagline: "Proven Strategies to Help Groups Get Unstuck"
Nice to have
• Showing diverse people, or hands. Diverse kinds of groups - not just business. A colorful cover. Maybe show the complexity of trust when it is broken...broken pieces of trust that are then picked up and put together when people work together. Could show people (or images of hands) or other ways to show that it's a choice and it is possible to repair broken trust. I'd also like to convey a sense of a group - not just random people. That they have something at stake to work on repairing trust together and this book can help them.
Should not have
• If images of people are used, just showing one gender or race is not okay. Nor just binary choices: like an image containing one man and one woman, or one white person and one person of color - otherwise it seems that the book on Lantern Hour is about race or gender relations.

```html
<!DOCTYPE html>
<html lang="en">
<head>
<meta charset="utf-8">
<title>Lantern Hour – Cover Spread</title>
<link rel="stylesheet" href="https://fonts.googleapis.com/css2?family=Marcellus&family=Open+Sans:wght@400;600&display=swap">
<style>
  :root {
    --stage: #d9dcdd;
    --teal-light: #2a8597;
    --teal: #1d6b7b;
    --teal-deep: #0f4653;
    --ivory: #ffffff;
    --soft-ivory: #dcebee;
    --muted-teal: #7fb0ba;
    --ink-red: #c8442e;
    --spine: #17606f;
  }
  * { margin: 0; padding: 0; box-sizing: border-box; }
  html, body { width: 1200px; height: 1200px; overflow: hidden; }
  body {
    background: var(--stage);
    display: flex;
    align-items: center;
    justify-content: center;
    font-family: "Marcellus", serif;
  }
  .cover-spread {
    display: flex;
    width: 1080px;
    height: 750px;
    box-shadow: 0 10px 30px rgba(0,0,0,0.18);
  }

  /* Back cover */
  .back-cover {
    position: relative;
    width: 500px;
    height: 100%;
    background: linear-gradient(160deg, var(--teal-light) 0%, var(--teal) 45%, var(--teal-deep) 100%);
    overflow: hidden;
  }
  .hands-art {
    position: absolute;
    left: 40px;
    top: 20px;
    width: 300px;
    height: 710px;
    background:
      radial-gradient(ellipse 60% 28% at 55% 18%, rgba(255,255,255,0.55), rgba(255,255,255,0) 70%),
      radial-gradient(ellipse 65% 32% at 50% 74%, rgba(255,255,255,0.6), rgba(255,255,255,0) 70%);
  }
  .publisher-mark {
    position: absolute;
    top: 34px;
    right: 38px;
    display: flex;
    align-items: center;
    gap: 8px;
    background: var(--ivory);
    padding: 6px 10px;
    font-family: "Marcellus", serif;
    font-size: 12px;
    letter-spacing: 0.08em;
    text-transform: uppercase;
    color: var(--teal-deep);
  }
  .publisher-mark .mark-square {
    width: 12px;
    height: 12px;
    background: var(--teal-deep);
  }

  /* Spine */
  .spine {
    width: 80px;
    height: 100%;
    background: linear-gradient(180deg, var(--teal) 0%, var(--spine) 55%, var(--teal-deep) 100%);
    display: flex;
    align-items: center;
    justify-content: center;
  }
  .spine-title {
    writing-mode: vertical-rl;
    display: flex;
    align-items: center;
    gap: 20px;
    color: var(--ivory);
    font-size: 30px;
    letter-spacing: 0.06em;
    white-space: nowrap;
  }
  .spine-struck {
    position: relative;
    display: inline-block;
    font-size: 16px;
    color: var(--muted-teal);
    padding: 2px 0;
  }
  .spine-struck svg {
    position: absolute;
    inset: 0;
    width: 100%;
    height: 100%;
  }
  .spine-small { font-size: 18px; }

  /* Front cover */
  .front-cover {
    position: relative;
    width: 500px;
    height: 100%;
    background: linear-gradient(165deg, var(--teal-light) 0%, var(--teal) 50%, var(--teal-deep) 100%);
    color: var(--ivory);
  }
  .frame-outer {
    position: absolute;
    inset: 26px;
    border: 4px solid var(--ivory);
  }
  .frame-inner {
    position: absolute;
    inset: 38px;
    border: 1.5px solid var(--ivory);
  }
  .front-content {
    position: absolute;
    inset: 38px;
    display: flex;
    flex-direction: column;
    align-items: center;
    text-align: center;
  }
  .book-title {
    margin-top: 66px;
    font-weight: 400;
    font-size: 74px;
    line-height: 1.02;
    letter-spacing: 0.03em;
    text-transform: uppercase;
  }
  .struck-phrase {
    position: relative;
    margin-top: 20px;
    font-size: 38px;
    line-height: 1;
    letter-spacing: 0.06em;
    color: var(--muted-teal);
    text-transform: uppercase;
  }
  .struck-phrase svg {
    position: absolute;
    left: -14px;
    top: -4px;
    width: calc(100% + 28px);
    height: calc(100% + 8px);
  }
  .affirmation {
    margin-top: 14px;
    font-size: 34px;
    line-height: 1;
    letter-spacing: 0.1em;
    text-transform: uppercase;
  }
  .possible-word {
    margin-top: 8px;
    font-size: 86px;
    letter-spacing: 0.04em;
    line-height: 1;
    text-transform: uppercase;
  }
  .tagline {
    margin-top: 34px;
    max-width: 340px;
    font-size: 19px;
    line-height: 1.4;
    letter-spacing: 0.04em;
    color: var(--soft-ivory);
  }
  .author-name {
    margin-top: auto;
    margin-bottom: 52px;
    font-size: 22px;
    letter-spacing: 0.03em;
  }
</style>
</head>
<body>
  <div class="cover-spread">
    <section class="back-cover">
      <div class="hands-art" role="img" aria-label="White silhouette illustration of two hands reaching toward each other"></div>
      <div class="publisher-mark"><span class="mark-square"></span>Harbor Lane Press</div>
    </section>

    <section class="spine">
      <div class="spine-title">
        <span>LANTERN HOUR</span>
        <span class="spine-struck">IS IT?
          <svg viewBox="0 0 10 10" preserveAspectRatio="none" aria-hidden="true">
            <line x1="1" y1="0" x2="9" y2="10" stroke="#c8442e" stroke-width="1.2"/>
            <line x1="9" y1="0" x2="1" y2="10" stroke="#c8442e" stroke-width="1.2"/>
          </svg>
        </span>
        <span class="spine-small">IT IS</span>
        <span>POSSIBLE</span>
      </div>
    </section>

    <section class="front-cover">
      <div class="frame-outer"></div>
      <div class="frame-inner"></div>
      <div class="front-content">
        <h1 class="book-title">Lantern<br>Hour</h1>
        <div class="struck-phrase">Is it?
          <svg viewBox="0 0 100 40" preserveAspectRatio="none" aria-hidden="true">
            <line x1="2" y1="36" x2="98" y2="6" stroke="#c8442e" stroke-width="3" stroke-linecap="round"/>
            <line x1="2" y1="8" x2="98" y2="32" stroke="#c8442e" stroke-width="3" stroke-linecap="round"/>
          </svg>
        </div>
        <div class="affirmation">It IS</div>
        <div class="possible-word">Possible</div>
        <p class="tagline">Proven Strategies to Help Groups Get Unstuck</p>
        <p class="author-name">Marla Quinby, Ph.D.</p>
      </div>
    </section>
  </div>
</body>
</html>
```